prestige web design for KELVA Finance

Hi Guys,

Looking to team up with a creative designer for another of our websites for KELVA finance.
if looking for our similar website www.brimlendco.com.au is one of our other companies. ideally working in our logo being black and white.

Please see attachments for our logo and a description
HOME
VEHICLE
EQUIPMENT
WHO WE ARE
CONTACT US

open to ideas on layout .

touch base if you have any questions.

Target Market(s)

Prestige cars and equipment -trucks earthmoving

Industry/Entity Type

finance

Coding

Coded - Design and coding required

Number of Pages Required

5+ page

Font styles to use
Sans Serif

Colors

Designer to choose colors to be used in the design.

```html
<!DOCTYPE html>
<html lang="en">
<head>
<meta charset="utf-8">
<title>KELVA Finance</title>
<link href="https://fonts.googleapis.com/css2?family=Montserrat:ital,wght@0,300;0,400;0,500;0,600;0,700;0,800;1,300;1,600;1,700;1,800&display=swap" rel="stylesheet">
<style>
:root{
  --ink:#111111;
  --white:#ffffff;
  --muted:#9a9a9a;
  --line:#d9d9d9;
  --blue:#1f3f8f;
  --footer-a:#101622;
  --footer-b:#2a2016;
  --form-bg:#c6c6c6;
}
*{margin:0;padding:0;box-sizing:border-box}
html,body{width:1200px;height:3363px;overflow:hidden;background:var(--white)}
body{position:relative;font-family:'Montserrat',sans-serif;color:var(--ink)}
.abs{position:absolute}

/* hero */
.hero-media{left:0;top:0;width:1200px;height:594px;background:linear-gradient(90deg,#d9d6d2 0%,#b98a5d 35%,#c78a52 50%,#e2d3b8 70%,#cfdde3 100%)}
.nav-bar{left:0;top:34px;width:1200px;height:60px;background:rgba(245,245,245,.82)}
.brand{left:18px;top:44px;height:40px;display:flex;align-items:center;gap:10px;font-weight:800;font-size:34px;letter-spacing:1px;color:var(--ink)}
.brand-mark{width:14px;height:14px;background:var(--ink)}
.nav{right:14px;top:44px;height:40px;display:flex;align-items:center;gap:34px;list-style:none}
.nav li{font-style:italic;font-weight:700;font-size:19px;color:var(--ink)}
.hero-title{left:0;width:1200px;text-align:center;font-style:italic;font-weight:800;font-size:62px;line-height:1}
.hero-title span{background:rgba(235,235,235,.82);padding:2px 14px;display:inline-block}

/* calculator */
.calc{left:104px;top:572px;width:951px;height:42px;display:flex;border:1.5px solid var(--blue);background:var(--white)}
.calc .field{height:100%;border-right:1px solid var(--line);display:flex;align-items:center;padding-left:8px;font-size:14px;letter-spacing:1.5px;color:var(--muted);font-style:italic}
.calc .cur{font-style:normal;font-size:30px;color:var(--ink);margin-right:8px;font-weight:500}
.calc .go{flex:1;background:var(--blue);color:var(--white);font-style:italic;font-weight:600;font-size:22px;display:flex;align-items:center;justify-content:center}

/* feature cards */
.card{left:80px;width:1039px;height:678px;border:1px solid #dcdcdc;box-shadow:0 1px 3px rgba(0,0,0,.15);background:var(--white)}
.card-media{width:452px;height:678px;top:0}
.card-body{font-size:22px;line-height:28.6px;letter-spacing:1.6px;font-weight:500}
.card h2{font-weight:800;font-size:52px;letter-spacing:1px}
.lockup{font-weight:800;letter-spacing:14px;line-height:1}
.lockup .big{font-size:66px;display:block}
.lockup .sub{font-size:28px;letter-spacing:7px;display:block;margin-top:2px}
.more{display:flex;align-items:center;gap:10px;font-style:italic;font-weight:800;font-size:16px;letter-spacing:1.5px}
.more svg{width:36px;height:36px}

/* footer */
.footer{left:0;top:2910px;width:1200px;height:453px;background:radial-gradient(circle at 70% 60%,#4a2e12 0%,transparent 55%),linear-gradient(135deg,var(--footer-a),var(--footer-b))}
.footer-brand{left:72px;top:2964px;display:flex;align-items:center;gap:10px;color:var(--white);font-weight:800;font-size:36px;letter-spacing:1px}
.footer-brand .brand-mark{background:var(--white)}
.footer-about{left:72px;top:3036px;width:490px;color:var(--white);font-style:italic;font-size:13.5px;line-height:17.5px;letter-spacing:.8px;font-weight:300}
.contact{left:72px;display:flex;align-items:center;gap:20px;color:var(--white);font-style:italic;font-weight:800;font-size:28px}
.contact .ico{width:30px;height:30px}
.form{left:691px;top:2939px;width:390px;height:392px;background:var(--form-bg)}
.form h3{position:absolute;left:31px;top:22px;font-style:italic;font-weight:800;font-size:17px;letter-spacing:1px}
.input{position:absolute;left:23px;width:345px;height:27px;background:var(--white);font-weight:800;font-size:13px;letter-spacing:4px;padding:5px 10px}
.submit{position:absolute;left:23px;top:314px;width:345px;height:27px;background:var(--ink);color:var(--white);font-weight:800;font-style:italic;font-size:14px;letter-spacing:4px;text-align:center;line-height:27px}
</style>
</head>
<body>

<header>
  <div class="abs hero-media" role="img" aria-label="Bright living room with a tan leather sofa, plant and timber slat divider"></div>
  <div class="abs nav-bar"></div>
  <div class="abs brand"><span class="brand-mark"></span>KELVA Finance</div>
  <ul class="abs nav">
    <li>HOME</li><li>VEHICLE</li><li>EQUIPMENT</li><li>WHO WE ARE</li><li>CONTACT US</li>
  </ul>
  <h1>
    <div class="abs hero-title" style="top:222px"><span>MAKERS</span></div>
    <div class="abs hero-title" style="top:302px"><span>OF</span></div>
    <div class="abs hero-title" style="top:378px"><span>POSSIBLE</span></div>
  </h1>
  <div class="abs calc">
    <div class="field" style="width:209px"><span class="cur">$</span>Purchasing amount</div>
    <div class="field" style="width:128px"><span class="cur">$</span>Deposit</div>
    <div class="field" style="width:114px;justify-content:space-between;padding-right:12px">Term
      <svg width="20" height="12" viewBox="0 0 20 12"><path d="M2 2l8 8 8-8" fill="none" stroke="#111" stroke-width="2"/></svg></div>
    <div class="field" style="width:143px">Interest Rate</div>
    <div class="field" style="width:170px">Balloon payment</div>
    <div class="go">CALCULATE</div>
  </div>
</header>

<main>
  <section class="abs card" style="top:670px">
    <div class="abs card-media" style="left:0;background:linear-gradient(180deg,#7fb0e0 0%,#cfe0ef 35%,#5a5a58 60%,#c4703e 100%)" role="img" aria-label="Building under construction wrapped in scaffolding"></div>
    <h2 class="abs" style="left:494px;top:52px">ABOUT US</h2>
    <p class="abs card-body" style="left:494px;top:128px;width:520px">KELVA Finance has nearly 20 years industry experience, so we certainly understand personal and business lending. We are committed to providing individuals and businesses with tailored financial services that enable them to reach and then exceed their financial goals. We have a vast list of lenders to suit along with an online team ready to help you, so we're easily accessible and here when you need us. Our friendly team of experienced and approachable staff that will listen, understand your situation and lend responsibly.</p>
    <div class="abs more" style="left:490px;top:598px"><svg viewBox="0 0 36 36"><circle cx="18" cy="18" r="16" fill="none" stroke="#111" stroke-width="2"/><path d="M14 12l6 6-6 6M18 12l6 6-6 6" fill="none" stroke="#111" stroke-width="1.5"/></svg>FIND MORE</div>
  </section>

  <section class="abs card" style="top:1421px">
    <div class="abs card-media" style="left:587px;background:linear-gradient(160deg,#8a7a70 0%,#cfcfcf 30%,#1a1a1a 55%,#0a0a0a 100%)" role="img" aria-label="Rear of a black prestige car with red tail light"></div>
    <div class="abs lockup" style="left:34px;top:74px"><span class="big">KELVA</span><span class="sub" style="margin-left:64px">CARS</span></div>
    <p class="abs card-body" style="left:34px;top:188px;width:490px">While you focus on getting the right car, we will focus on getting you the right finance. Whether you're interested in purchasing a used or new car for yourself or a fleet of vehicles through your business, KELVA's team are well equipped to help you find the car finance that's right for you.</p>
    <div class="abs more" style="left:28px;top:496px"><svg viewBox="0 0 36 36"><circle cx="18" cy="18" r="16" fill="none" stroke="#111" stroke-width="2"/><path d="M14 12l6 6-6 6M18 12l6 6-6 6" fill="none" stroke="#111" stroke-width="1.5"/></svg>FIND MORE</div>
  </section>

  <section class="abs card" style="top:2164px">
    <div class="abs card-media" style="left:0;background:linear-gradient(170deg,#4f8fd0 0%,#c7dcef 40%,#3e7c80 60%,#7a4a2a 100%)" role="img" aria-label="Excavator bucket tipping soil against a blue sky"></div>
    <div class="abs lockup" style="left:494px;top:68px"><span class="big">KELVA</span><span class="sub" style="margin-left:4px">EQUIPMENT</span></div>
    <p class="abs card-body" style="left:494px;top:182px;width:500px">At KELVA, we help businesses of all sizes to secure funding in the form of a business loan for asset purchases from either a bank or private lender. Our dedicated Equipment Finance specialists have extensive industry experience across the agricultural, construction and earthmoving sectors. We'll work with you to understand the specific needs that face your business to keep your equipment up to date.</p>
    <div class="abs more" style="left:490px;top:570px"><svg viewBox="0 0 36 36"><circle cx="18" cy="18" r="16" fill="none" stroke="#111" stroke-width="2"/><path d="M14 12l6 6-6 6M18 12l6 6-6 6" fill="none" stroke="#111" stroke-width="1.5"/></svg>FIND MORE</div>
  </section>
</main>

<footer>
  <div class="abs footer" role="img" aria-label="Dark background with glowing workshop sparks"></div>
  <div class="abs footer-brand"><span class="brand-mark"></span>KELVA Finance</div>
  <p class="abs footer-about">KELVA Finance's aim is to build on the KELVA business track record and set a new benchmark in the Australian property finance industry, providing a good old fashioned localization service that delivers the assets you want when needed and structured to recognize the useful life of cash flow sensitive assets.</p>
  <div class="abs contact" style="top:3144px"><svg class="ico" viewBox="0 0 30 30"><path d="M9 5l4 5-2.5 3a14 14 0 0 0 6.5 6.5L20 17l5 4-2 4C14 25 5 16 5 7z" fill="none" stroke="#fff" stroke-width="2" stroke-linejoin="round"/></svg>0400 555 218</div>
  <div class="abs contact" style="top:3194px"><svg class="ico" viewBox="0 0 30 30"><circle cx="15" cy="15" r="11" fill="none" stroke="#fff" stroke-width="2.5"/></svg>KELVAOFFICIAL</div>
  <div class="abs contact" style="top:3244px"><svg class="ico" viewBox="0 0 30 30"><circle cx="15" cy="15" r="11" fill="none" stroke="#fff" stroke-width="2.5"/></svg>KELVAOFFICIAL</div>

  <form class="abs form">
    <h3>FILL THIS FROM TO GET IN TOUCH</h3>
    <div class="input" style="top:64px">NAME</div>
    <div class="input" style="top:113px">PHONE NUMBER</div>
    <div class="input" style="top:162px">EMAIL ADDRESS</div>
    <div class="input" style="top:217px;height:83px">MESSAGE</div>
    <div class="submit">SUBMIT</div>
  </form>
</footer>

</body>
</html>
```